Roster'd book cover required for a novel! Print and Ebook- Please see attached image

MY PEN NAME IS MARA HOLT.
Apologies to everyone that I have updated my brief.
On the front cover I would like Roster'd written in quite bold font (modern) and an image of an out line (silhouette) of a woman (Just like would be on a toilet door for women) holding hands with the silhouette of a domestic plane. I imagine the silhouettes to be black or dark grey and the font to be red with a white background.
Updates

Project Deadline Extended
Reason: I have struggled with my brief to know what to ask designers for but I have come up with a better idea and would love to extend to see if my brief is much clearer xx

Target Market(s)

Women

Industry/Entity Type

Book Publisher

Font styles to use
Serif
Sans Serif

Colors

Designer to choose colors to be used in the design.

Requirements
Must have
• Front, back and spine for a paperback and also a design for an ebook.
• Blurb: FIFO, the other four lettered F word.
• Roster’d tells the story of three women who swing from time with their fly-in fly-out lovers to time alone.
• Tessa swings from one week with Gary, to two weeks without. She is strong, messy and full of heart. Can she survive the chaos and the separation?
• Tessa’s younger sister, Nina, swings from one week with Rob, to three weeks alone. She craves attention and goes looking for it in likely places. Nina is not sure that one week in a month is enough for a marriage to survive.
• Nina doesn’t know that Rob also spends one week with Dora, who then spends three weeks by herself. Dora has lost the blueprint that was going to lead her somewhere fabulous. She lost her mother and her bearings. With a new job researching women in violent relationships, she is trying to work it all out.
• This is a story of dirt, coastal froth, loneliness, airports, fish, rosters, phone calls, mines, distance, time, country, independence, stars, laughter, sex and imperfect days.
• A white rectangle for an ISBN number on the back cover.
Nice to have
• As above

```html
<!DOCTYPE html>
<html lang="en">
<head>
<meta charset="utf-8">
<title>Roster'd — Book Cover Wrap</title>
<link rel="stylesheet" href="https://fonts.googleapis.com/css2?family=Barlow+Condensed:wght@600;700&family=Jost:wght@400&display=swap">
<style>
  :root {
    --signal-red: #d7262e;
    --paper: #ffffff;
    --charcoal: #3a3a3c;
    --charcoal-soft: #4a4a4d;
    --page: #ffffff;
    --spine-rule: #e3e3e3;
  }
  * { box-sizing: border-box; margin: 0; padding: 0; }
  html, body {
    width: 1200px; height: 633px; overflow: hidden;
    background: var(--page);
  }
  .canvas { position: relative; width: 1200px; height: 633px; }
  .cover-wrap {
    position: absolute; left: 194px; top: 16px;
    width: 811px; height: 600px;
    background: var(--paper);
    overflow: hidden;
    box-shadow: 0 2px 10px rgba(0,0,0,0.16);
  }

  /* back cover */
  .back-cover {
    position: absolute; left: 0; top: 0;
    width: 290px; height: 600px;
    background: var(--signal-red);
    color: var(--paper);
  }
  .back-tagline {
    position: absolute; left: 58px; top: 72px;
    font-family: "Barlow Condensed", sans-serif;
    font-weight: 600; font-size: 29px; line-height: 1.22;
    white-space: nowrap;
  }
  .back-blurb {
    position: absolute; left: 58px; top: 180px; width: 196px;
    font-family: "Jost", sans-serif;
    font-size: 8.8px; line-height: 12.8px;
    text-align: justify;
  }
  .back-blurb span { display: block; }
  .isbn-block {
    position: absolute; left: 58px; top: 512px;
    width: 124px; height: 58px;
    background: var(--paper);
  }

  /* spine */
  .spine {
    position: absolute; left: 385px; top: 0;
    width: 41px; height: 600px;
    border-left: 1px solid var(--spine-rule);
    border-right: 1px solid var(--spine-rule);
  }
  .spine-text {
    position: absolute; left: 50%;
    transform: translateX(-50%);
    writing-mode: vertical-rl;
    font-family: "Barlow Condensed", sans-serif;
    font-weight: 700; font-size: 20px; letter-spacing: 0.5px;
    color: var(--signal-red);
    white-space: nowrap;
  }
  .spine-title { top: 168px; }
  .spine-author { top: 276px; }

  /* front cover */
  .artwork { position: absolute; left: 0; top: 0; }
  .silhouette-area { fill: var(--charcoal-soft); }
  .flight-path { fill: var(--charcoal); }
  .front-title {
    position: absolute; left: 430px; top: 250px; width: 381px;
    text-align: center;
    font-family: "Barlow Condensed", sans-serif;
    font-weight: 700; font-size: 108px; line-height: 1;
    color: var(--signal-red);
    white-space: nowrap;
  }
  .front-author {
    position: absolute; left: 430px; top: 512px; width: 381px;
    text-align: center;
    font-family: "Barlow Condensed", sans-serif;
    font-weight: 700; font-size: 42px; line-height: 1;
    color: var(--signal-red);
  }
</style>
</head>
<body>
<main class="canvas">
  <section class="cover-wrap">
    <aside class="back-cover">
      <h2 class="back-tagline">FIFO, the other<br>four letter F word.</h2>
      <p class="back-blurb">
        <span>Roster’d tells the story of three women who swing from time with their fly-in fly-out lovers to time alone.</span>
        <span>Tessa swings from one week with Gary, to two weeks without. She is strong, messy and full of heart. Can she survive the chaos and the separation?</span>
        <span>Tessa’s younger sister, Nina, swings from one week with Rob, to three weeks alone. She craves attention and goes looking for it in likely places. Nina is not sure that one week in a month is enough for a marriage to survive.</span>
        <span>Nina doesn’t know that Rob also spends one week with Dora, who then spends three weeks by herself. Dora has lost the blueprint that was going to lead her somewhere fabulous. She lost her mother and her bearings. With a new job researching women in violent relationships, she is trying to work it all out.</span>
        <span>This is a story of dirt, coastal froth, loneliness, airports, fish, rosters, phone calls, mines, distance, time, country, independence, stars, laughter, sex and imperfect days.</span>
      </p>
      <div class="isbn-block" aria-label="ISBN space"></div>
    </aside>

    <svg class="artwork" width="811" height="600" viewBox="0 0 811 600">
      <rect class="silhouette-area" x="468" y="46" width="306" height="180" rx="4"
            role="img" aria-label="Dark grey silhouette of a woman, like a restroom door sign figure, holding hands with the silhouette of a small domestic plane"/>
      <g class="flight-path">
        <rect x="452" y="444" width="34" height="12"/>
        <rect x="508" y="442" width="34" height="12"/>
        <rect x="564" y="440" width="34" height="12"/>
        <rect x="620" y="438" width="34" height="12"/>
        <rect x="676" y="436" width="34" height="12"/>
        <rect x="732" y="435" width="22" height="12"/>
        <polygon points="746,424 772,441 748,460 741,452 755,441 739,432"/>
      </g>
    </svg>

    <div class="spine">
      <span class="spine-text spine-title">Roster’d</span>
      <span class="spine-text spine-author">MARA HOLT</span>
    </div>

    <h1 class="front-title">Roster’d</h1>
    <p class="front-author">MARA HOLT</p>
  </section>
</main>
</body>
</html>
```